Kelvora Ledger Web Design Contest

We would like for you to design a website for www.kelvoraledger-example.com. Kelvora Ledger is a CPA Firm offering accounting, auditing, and tax preparation services.

We would like to have a consistent feel with the logo, business card, envelope, and stationary designs that were created by another designer on PlanHive. Examples of each are attached. We would like the website to have a clean/modern style.

The website should include the following:

1. A general "Welcome" landing page
2. A "About the Company" page
3. A "Services Offered" page
4. A "Contact Us" form
5. A button for "Sign up for Newsletter"

Target Market(s)

Individuals and businesses that require accounting, auditing, and tax preparation services from a CPA.

Industry/Entity Type

Accounting

Coding

Number of Pages Required

5+ page

Font styles to use
Other font styles liked:
• Trebuchet or similar

Requirements
Must have
• Consistent feel with logo and letterhead. The gray and blue bar on the letterhead should be incorporated into the website design.

```html
<!DOCTYPE html>
<html lang="en">
<head>
<meta charset="utf-8">
<title>Kelvora Ledger — Accounting · Audit · Tax Services</title>
<link rel="stylesheet" href="https://fonts.googleapis.com/css2?family=Arimo:wght@400;500&family=Questrial&display=swap">
<style>
  :root {
    --navy: #00226e;
    --navy-text: #1a2f6e;
    --charcoal: #4f4f4f;
    --button-gray: #8c8c8c;
    --page-bg: #ffffff;
    --header-bg: #e9e9e9;
    --divider: #e6e5ec;
    --ink: #111111;
    --hero-light: #d7e0ec;
    --hero-mid: #a9b9cf;
    --hero-deep: #7f93b1;
  }
  * { box-sizing: border-box; margin: 0; padding: 0; }
  html, body { width: 1079px; height: 1200px; overflow: hidden; }
  body {
    position: relative;
    background: var(--page-bg);
    font-family: "Arimo", Arial, sans-serif;
    color: var(--ink);
  }

  /* Top bar */
  .top-strip { position: absolute; left: 0; top: 0; width: 1079px; height: 70px; background: var(--header-bg); }
  .top-bars { position: absolute; left: 0; top: 0; }
  .main-nav { position: absolute; top: 14px; left: 0; height: 56px; display: flex; align-items: center; }
  .main-nav a {
    position: absolute; white-space: nowrap;
    font-family: "Questrial", "Century Gothic", sans-serif;
    font-size: 19px; color: #fff; text-decoration: none; letter-spacing: 0.2px;
  }
  .newsletter-button {
    position: absolute; left: 873px; top: 29px; width: 171px; height: 24px;
    background: var(--button-gray); color: #fff; border: 0;
    font-family: "Arimo", Arial, sans-serif; font-size: 13.5px;
    display: flex; align-items: center; justify-content: center;
  }

  /* Brand header */
  .brand-header {
    position: absolute; top: 70px; left: 0; width: 1079px; height: 142px;
    background: radial-gradient(ellipse at center, #fbfbfb 0%, #f1f1f1 60%, #e4e4e4 100%);
  }
  .brand-mark {
    position: absolute; left: 506px; top: 11px; width: 73px; height: 73px;
    border: 4px solid #444;
  }
  .brand-name {
    position: absolute; top: 92px; left: 0; width: 1079px; text-align: center;
    font-size: 21px; font-weight: 500; color: var(--navy-text); letter-spacing: 1px;
  }
  .brand-rule { position: absolute; left: 396px; top: 118px; width: 294px; height: 1px; background: var(--navy-text); }
  .brand-tagline {
    position: absolute; top: 121px; left: 0; width: 1079px; text-align: center;
    font-size: 12.5px; color: #333; letter-spacing: 1.6px;
  }

  /* Hero slider */
  .hero { position: absolute; top: 212px; left: 0; width: 1079px; height: 400px; }
  .hero-photo {
    position: absolute; inset: 0;
    background: linear-gradient(120deg, var(--hero-mid) 0%, var(--hero-light) 35%, #e8eef5 55%, var(--hero-mid) 80%, var(--hero-deep) 100%);
  }
  .hero-card {
    position: absolute; left: 212px; top: 120px; width: 646px; height: 186px;
    background: rgba(255,255,255,0.72); text-align: center;
  }
  .hero-card h2 { margin-top: 30px; font-size: 18px; font-weight: 400; color: var(--ink); }
  .hero-card p { margin: 10px auto 0; width: 560px; font-size: 15px; line-height: 21.5px; color: #222; }
  .learn-more {
    display: inline-flex; align-items: center; justify-content: center;
    margin-top: 14px; width: 114px; height: 24px; background: var(--navy);
    color: #fff; font-size: 13.5px; text-decoration: none;
  }
  .slider-arrow { position: absolute; top: 165px; }
  .slider-arrow.prev { left: 34px; }
  .slider-arrow.next { left: 1006px; }
  .hero-divider { position: absolute; top: 612px; left: 0; width: 1079px; height: 14px; background: var(--divider); }

  /* Services */
  .service { position: absolute; top: 697px; width: 290px; text-align: center; }
  .service-photo { width: 170px; height: 170px; border-radius: 50%; margin: 0 auto; }
  .service h3 { margin-top: 18px; font-size: 18px; font-weight: 500; color: var(--ink); }
  .service p { margin-top: 16px; font-size: 15px; line-height: 21px; color: #1c1c1c; }
  .service-tax { left: 69px; }
  .service-tax .service-photo { background: radial-gradient(circle at 40% 40%, #d9e4ee, #8ea6bd 70%, #5d7890); }
  .service-accounting { left: 390px; }
  .service-accounting .service-photo { background: radial-gradient(circle at 50% 40%, #f1f1f4, #c9c4d9 55%, #8b78b8 80%, #e36a3a); }
  .service-auditing { left: 699px; }
  .service-auditing .service-photo { background: radial-gradient(circle at 50% 45%, #f4f4f4, #d5d7da 55%, #3b3b3b 95%); }

  /* Footer */
  .site-footer { position: absolute; left: 0; top: 1140px; width: 1079px; height: 60px; }
  .copyright {
    position: absolute; left: 156px; top: 33px;
    font-size: 14.5px; color: #fff;
  }
  .social-links { position: absolute; left: 796px; top: 19px; display: flex; gap: 32px; }
  .social-links span { width: 18px; height: 18px; border-radius: 50%; background: #fff; display: block; }
</style>
</head>
<body>

<header>
  <div class="top-strip"></div>
  <svg class="top-bars" width="1079" height="70" viewBox="0 0 1079 70" aria-hidden="true">
    <polygon points="630,0 1079,0 1079,68 584,68" fill="var(--charcoal)"/>
    <polygon points="0,14 604,14 584,70 0,70" fill="var(--navy)"/>
    <rect x="0" y="68" width="584" height="2" fill="#13307a"/>
  </svg>
  <nav class="main-nav">
    <a href="#" style="left:19px">HOME</a>
    <a href="#" style="left:154px">About Us</a>
    <a href="#" style="left:304px">Services</a>
    <a href="#" style="left:455px">Contact Us</a>
  </nav>
  <button class="newsletter-button" type="button">Sign up for Newsletter</button>

  <div class="brand-header">
    <div class="brand-mark"></div>
    <div class="brand-name">KELVORA LEDGER, LLC</div>
    <div class="brand-rule"></div>
    <div class="brand-tagline">Accounting · Audit · Tax Services</div>
  </div>
</header>

<section class="hero">
  <div class="hero-photo" role="img" aria-label="Soft blue-toned photo of a calculator, coins and printed financial tables"></div>
  <div class="hero-card">
    <h2>Tax preparation services</h2>
    <p>Nunc ac magna. Maecenas odio dolor, vulputate vel, auctor ac, accumsan id, felis. Pellentesque cursus sagittis felis. Pellentesque porttitor, velit lacinia egestas auctor, diam eros tempus arcu, nec vulputate augue magna vel risus.</p>
    <a class="learn-more" href="#">Learn More...</a>
  </div>
  <svg class="slider-arrow prev" width="38" height="84" viewBox="0 0 38 84" aria-label="Previous slide">
    <polyline points="36,2 2,42 36,82" fill="none" stroke="#fff" stroke-width="1.3"/>
  </svg>
  <svg class="slider-arrow next" width="38" height="84" viewBox="0 0 38 84" aria-label="Next slide">
    <polyline points="2,2 36,42 2,82" fill="none" stroke="#fff" stroke-width="1.3"/>
  </svg>
</section>
<div class="hero-divider"></div>

<main>
  <article class="service service-tax">
    <div class="service-photo" role="img" aria-label="Close-up photo of a calculator keypad"></div>
    <h3>Tax preparation services</h3>
    <p>Nunc ac magna. Maecenas odio dolor, vulputate vel, auctor ac, accumsan id, felis. Pellentesque cursus sagittis felis. Pellentesque porttitor, velit lacinia eges-tas auctor, diam eros tempus arcu, nec vulputate augue magna vel risus.</p>
  </article>
  <article class="service service-accounting">
    <div class="service-photo" role="img" aria-label="Photo of printed colourful bar and pie charts with a pen"></div>
    <h3>Accounting</h3>
    <p>Nunc ac magna. Maecenas odio dolor, vulputate vel, auctor ac, accumsan id, felis. Pellentesque cursus sagittis felis. Pellentesque porttitor, velit lacinia eges-tas auctor, diam eros tempus arcu, nec vulputate augue magna vel risus.</p>
  </article>
  <article class="service service-auditing">
    <div class="service-photo" role="img" aria-label="Photo of hands reviewing documents beside a computer keyboard"></div>
    <h3>Auditing</h3>
    <p>Nunc ac magna. Maecenas odio dolor, vulputate vel, auctor ac, accumsan id, felis. Pellentesque cursus sagittis felis. Pellentesque porttitor, velit lacinia eges-tas auctor, diam eros tempus arcu, nec vulputate augue magna vel risus.</p>
  </article>
</main>

<footer class="site-footer">
  <svg width="1079" height="60" viewBox="0 0 1079 60" aria-hidden="true" style="position:absolute;left:0;top:0">
    <polygon points="656,0 1079,0 1079,60 608,60" fill="var(--charcoal)"/>
    <polygon points="0,14 628,14 592,58 0,58" fill="var(--navy)"/>
  </svg>
  <div class="copyright">Copyright © 2015 Kelvora Ledger</div>
  <div class="social-links">
    <span role="img" aria-label="Social link"></span>
    <span role="img" aria-label="Social link"></span>
    <span role="img" aria-label="Social link"></span>
    <span role="img" aria-label="Social link"></span>
  </div>
</footer>

</body>
</html>
```